Create Vertical Dog Food Labels (3 inches x 5 inches) for PupKitchen

We need a packing Vertical label (3 inches x 5 inches) design for our line of Dog Food - Pup Kitchen at pupkitchenmeals.com (please review website). This design is for Custom Roll Labels. We have a logo already. Use our logo colors on label. What we need incorporated is a list of our ingredients:

50% Choice Beef
20% Pasture-raised Chicken
15% Brown Rice
15% Fresh Vegetables - Carrots, Kale, Zucchini
Herbal Health Boosters

We also need these lines at the bottom of the label:

Keeps in fridge for 4 days after thawing
Stores in freezer up to 6 months
Questions? email us at orders@meadowlanepantry.com

We have attached a sample of a competitor. The Kibble Crate.

Target Market(s)

Dog owners

Industry/Entity Type

Dog Food

Font styles to use
Sans Serif

Requirements
Must have
• Read project description above
Nice to have
• Our logo color incorporated
Should not have
• I want it simple.

```html
<!DOCTYPE html>
<html lang="en">
<head>
<meta charset="utf-8">
<title>PupKitchen – Dog Food Label</title>
<link rel="stylesheet" href="https://fonts.googleapis.com/css2?family=Montserrat:wght@500;600;700&display=swap">
<style>
  :root {
    --backdrop: #3b3b3b;
    --label-bg: #ffffff;
    --brand-green: #2f8f3f;
    --beef: #f07a4a;
    --chicken: #f5a623;
    --rice: #f7b77c;
    --veg: #7cb342;
    --herbal: #6aa84f;
    --storage: #1f9a4b;
    --mark-green: #5aa845;
  }
  * { box-sizing: border-box; margin: 0; padding: 0; }
  html, body {
    width: 1200px; height: 924px; overflow: hidden;
    background: var(--backdrop);
    font-family: "Montserrat", sans-serif;
  }
  .label {
    position: absolute; left: 338px; top: 32px;
    width: 524px; height: 860px;
    background: var(--label-bg);
  }
  .brand-mark {
    position: absolute; left: 192px; top: 70px;
    width: 140px; height: 140px; border-radius: 50%;
    background: var(--mark-green);
  }
  .brand-name {
    position: absolute; left: 0; right: 0; top: 232px;
    text-align: center; font-weight: 600; font-size: 58px;
    color: var(--brand-green); letter-spacing: -0.5px;
  }
  .ingredient {
    position: absolute; left: 0; right: 0; height: 40px;
    display: flex; align-items: center;
  }
  .ingredient__pct {
    height: 100%; display: flex; align-items: center; justify-content: center;
    color: #fff; font-weight: 700; font-size: 24px;
  }
  .ingredient__name {
    flex: 1; height: 100%;
    display: flex; align-items: center; justify-content: center;
    border-top: 2px dashed currentColor; border-bottom: 2px dashed currentColor;
    font-weight: 500; font-size: 17px; opacity: 0.85;
  }
  .ingredient--beef { top: 387px; color: var(--beef); }
  .ingredient--beef .ingredient__pct { width: 50%; background: var(--beef); }
  .ingredient--chicken { top: 455px; color: var(--chicken); }
  .ingredient--chicken .ingredient__pct { width: 20%; background: var(--chicken); }
  .ingredient--rice { top: 514px; color: var(--rice); }
  .ingredient--rice .ingredient__pct { width: 15%; background: var(--rice); }
  .ingredient--veg { top: 581px; color: var(--veg); }
  .ingredient--veg .ingredient__pct { width: 15%; background: var(--veg); }
  .herbal-band {
    position: absolute; left: 6px; right: 0; top: 646px; height: 40px;
    background: var(--herbal); color: #fff;
    display: flex; align-items: center; justify-content: center;
    font-weight: 600; font-size: 18px;
  }
  .storage-band {
    position: absolute; left: 0; right: 0; top: 745px; height: 62px;
    background: var(--storage); color: #fff; text-align: center;
    display: flex; flex-direction: column; justify-content: center;
    font-weight: 600; font-size: 17px; line-height: 1.3;
  }
  .contact {
    position: absolute; left: 0; right: 0; top: 818px;
    text-align: center; color: var(--brand-green);
    font-weight: 700; font-size: 16.5px;
  }
</style>
</head>
<body>
  <main class="label">
    <div class="brand-mark"></div>
    <h1 class="brand-name">PupKitchen</h1>

    <div class="ingredient ingredient--beef">
      <span class="ingredient__pct">50%</span>
      <span class="ingredient__name">Choice Beef</span>
    </div>
    <div class="ingredient ingredient--chicken">
      <span class="ingredient__pct">20%</span>
      <span class="ingredient__name">Pasture-raised Chicken</span>
    </div>
    <div class="ingredient ingredient--rice">
      <span class="ingredient__pct">15%</span>
      <span class="ingredient__name">15% Brown Rice</span>
    </div>
    <div class="ingredient ingredient--veg">
      <span class="ingredient__pct">15%</span>
      <span class="ingredient__name">15% Fresh Vegetables - Carrots, Kale, Zucchini</span>
    </div>

    <div class="herbal-band">Herbal Health Boosters</div>

    <div class="storage-band">
      <span>Keeps in fridge for 4 days after thawing</span>
      <span>Stores in freezer up to 6 months</span>
    </div>

    <p class="contact">Questions? email us at orders@meadowlanepantry.com</p>
  </main>
</body>
</html>
```